Package design for a set of baby wood brush

It has to be different from the competitions - here are the competitions, the box is the same size and shape, but I want the design to be different then others and stick out, yet to be suitable as baby product and baby shower gift.
I am going to call it "a quiet pine morning" it will be printed on the brush itself.
1) https://www.velmarket.com/MIRUbaby-Newborns-Toddlers-Bristles-Registry/dp/K47TQZ2R8X/ref=sr_1_7_a_it?ie=UTF8&qid=1357924680&sr=8-7&keywords=baby+brush
2) https://www.velmarket.com/Newborns-Toddlers-Natural-Bristles-Registry/dp/K47PVNHJQC/ref=sr_1_17_a_it?ie=UTF8&qid=1357924752&sr=8-17&keywords=baby+brush
3) https://www.velmarket.com/BabyTermas-Silicone-Newborns-Toddlers-Bristles/dp/K52ZH8T31J/ref=sr_1_21_a_it?ie=UTF8&qid=1358016384&sr=8-21&keywords=baby+wood+brush
The desighn should be different then the competitors but still transmit a natural baby product. there will also be a little text and a naturlality symbols.
Thanks

```html
<!DOCTYPE html>
<html lang="en">
<head>
<meta charset="utf-8">
<title>a quiet pine morning – Baby Wooden Hairbrush Set</title>
<link rel="stylesheet" href="https://fonts.googleapis.com/css2?family=Arvo:wght@400;700&family=Oswald:wght@600&family=Sniglet:wght@800&display=swap">
<style>
  :root {
    --page: #ffffff;
    --box-cream: #f6f8e6;
    --band-green: #8dbb4c;
    --frame-green: #9cc65a;
    --title-brown: #5a4330;
    --script-purple: #6b3b7e;
    --copy-green: #5f8a35;
    --ornament-yellow: #f2d36a;
    --wood-light: #e6bf8a;
    --wood-mid: #cf9c62;
    --bristle: #efe1b8;
    --badge-ring: #c9a45c;
    --badge-fill: #fbf6e6;
    --rule: #b9c99a;
  }
  html, body {
    margin: 0;
    padding: 0;
    width: 1200px;
    height: 1200px;
    overflow: hidden;
    background: var(--page);
  }
  .canvas {
    position: relative;
    width: 1200px;
    height: 1200px;
  }
  .product-photo {
    position: absolute;
  }
  .product-photo--massage-brush {
    left: 272px; top: 336px; width: 152px; height: 524px;
    border-radius: 76px 76px 40px 40px / 130px 130px 60px 60px;
    background: linear-gradient(180deg, var(--wood-light) 0%, var(--wood-mid) 45%, var(--wood-light) 100%);
  }
  .product-photo--soft-brush {
    left: 772px; top: 316px; width: 140px; height: 524px;
    border-radius: 70px 70px 36px 36px / 130px 130px 60px 60px;
    background: linear-gradient(180deg, var(--bristle) 0%, var(--bristle) 40%, var(--wood-mid) 55%, var(--wood-light) 100%);
  }
  .box {
    position: absolute;
    left: 458px; top: 246px;
    width: 284px; height: 620px;
    background: var(--box-cream);
    overflow: hidden;
    font-family: 'Arvo', serif;
    text-align: center;
  }
  .box__botanical-backdrop {
    position: absolute; inset: 0;
    background:
      radial-gradient(ellipse 70% 30% at 50% 28%, rgba(240, 214, 160, 0.35), transparent 70%),
      radial-gradient(ellipse 80% 35% at 50% 80%, rgba(190, 205, 225, 0.35), transparent 70%),
      linear-gradient(180deg, #f7f8e8 0%, #eef3df 100%);
  }
  .box__band {
    position: absolute; left: 0; right: 0; height: 13px;
    background: var(--band-green);
  }
  .box__band--top { top: 0; }
  .box__band--bottom { bottom: 0; height: 14px; }
  .box__trim {
    position: absolute; left: 10px; right: 10px; height: 26px;
    background: linear-gradient(90deg, rgba(242, 211, 106, 0.55), rgba(160, 200, 110, 0.45), rgba(242, 211, 106, 0.55));
    border-radius: 13px;
  }
  .box__trim--top { top: 16px; }
  .box__trim--bottom { top: 566px; }
  .brand-name {
    position: absolute; left: 0; right: 0; top: 62px;
    margin: 0;
    font-family: 'Arvo', serif;
    font-weight: 700;
    font-size: 25px;
    line-height: 1.05;
    color: var(--copy-green);
  }
  .mascot {
    position: absolute; left: 108px; top: 128px;
    width: 70px; height: 64px;
    border-radius: 50%;
    background: radial-gradient(circle, #fff6cf 0%, #f5dc7a 70%, rgba(245, 220, 122, 0) 100%);
  }
  .title-frame {
    position: absolute; left: 50px; top: 198px;
    width: 184px; height: 106px;
    box-sizing: border-box;
    border: 2px solid var(--frame-green);
    border-radius: 26px;
    display: flex; align-items: center; justify-content: center;
  }
  .product-title {
    margin: 0;
    font-family: 'Oswald', sans-serif;
    font-weight: 600;
    font-size: 23px;
    line-height: 28px;
    letter-spacing: 0.5px;
    color: var(--title-brown);
    text-transform: uppercase;
  }
  .feature-list {
    position: absolute; left: 0; right: 0; top: 318px;
    margin: 0; padding: 0; list-style: none;
  }
  .feature {
    margin: 0 auto;
    width: 196px;
    padding: 2px 0 5px;
    border-bottom: 1px dashed var(--rule);
  }
  .feature + .feature { margin-top: 6px; }
  .feature__name {
    display: block;
    font-family: 'Sniglet', cursive;
    font-weight: 800;
    font-size: 17px;
    line-height: 20px;
    color: var(--script-purple);
  }
  .feature__note {
    display: block;
    font-size: 11.5px;
    line-height: 15px;
    color: var(--copy-green);
    white-space: nowrap;
    margin: 0 -30px;
  }
  .seals {
    position: absolute; left: 0; right: 0; top: 471px;
    display: flex; justify-content: center; gap: 20px;
  }
  .seal {
    width: 68px; height: 68px;
  }
</style>
</head>
<body>
<main class="canvas">
  <div class="product-photo product-photo--massage-brush" role="img" aria-label="Photo of the wooden massage hairbrush with wooden pin bristles"></div>

  <section class="box">
    <div class="box__botanical-backdrop" role="img" aria-label="Faint botanical illustration of pale flowers and leaves"></div>
    <div class="box__band box__band--top"></div>
    <div class="box__trim box__trim--top" role="img" aria-label="Playful wavy yellow and green dotted border"></div>

    <h1 class="brand-name">a quiet pine<br>morning</h1>
    <div class="mascot" role="img" aria-label="Little smiling flower mascot"></div>

    <div class="title-frame">
      <h2 class="product-title">Baby Wooden<br>Hairbrush Set</h2>
    </div>

    <ul class="feature-list">
      <li class="feature">
        <span class="feature__name">Soft Hairbrush</span>
        <span class="feature__note">made with natural goat hairt bristles</span>
      </li>
      <li class="feature">
        <span class="feature__name">Massage Hairbrush</span>
        <span class="feature__note">made with wooden bristles</span>
      </li>
      <li class="feature">
        <span class="feature__name">Wooden Comb</span>
        <span class="feature__note">perfect for a great look</span>
      </li>
    </ul>

    <div class="seals">
      <svg class="seal" viewBox="0 0 68 68" aria-hidden="true"><circle cx="34" cy="34" r="31" fill="var(--badge-fill)" stroke="var(--badge-ring)" stroke-width="3"/></svg>
      <svg class="seal" viewBox="0 0 68 68" aria-hidden="true"><circle cx="34" cy="34" r="31" fill="var(--badge-fill)" stroke="var(--badge-ring)" stroke-width="3"/></svg>
      <svg class="seal" viewBox="0 0 68 68" aria-hidden="true"><circle cx="34" cy="34" r="31" fill="var(--badge-fill)" stroke="var(--badge-ring)" stroke-width="3"/></svg>
    </div>

    <div class="box__trim box__trim--bottom" role="img" aria-label="Playful wavy yellow and green dotted border"></div>
    <div class="box__band box__band--bottom"></div>
  </section>

  <div class="product-photo product-photo--soft-brush" role="img" aria-label="Photo of the wooden soft hairbrush with natural goat hair bristles"></div>
</main>
</body>
</html>
```